Hvac and insulation company needs good looking business card design

We are hvac and insulation company and looking for a new business cards that look to today standards designs

Target Market(s)

homeowners

Industry/Entity Type

Hvac

Contact Information for Business Card

Name: Dorian Velkova
Home comfort consultant
address: 4827 Marrow Ridge Rd #215 Oakland, CA 94611
office: 888-317-5069
cell: 510-642-1388
Lic.# 458127
Email: dorian@quarry-hvac.com
Web: quarry-hvac.com

Requirements
Must have
• clean and sleek look
Nice to have
• simple with a clean look
Should not have
• to busy business card

```html
<!DOCTYPE html>
<html lang="en">
<head>
<meta charset="utf-8">
<title>Quarry Home Solutions – Business Card</title>
<link rel="stylesheet" href="https://fonts.googleapis.com/css2?family=Open+Sans:wght@400;600;700&display=swap">
<style>
  :root {
    --backdrop: #1c1c1c;
    --card: #141414;
    --accent: #f7891f;
    --text: #f2f2f2;
    --silver: #c9c9c9;
    --muted: #9a9a9a;
  }
  * { margin: 0; padding: 0; box-sizing: border-box; }
  html, body {
    width: 1200px;
    height: 900px;
    overflow: hidden;
    background: var(--backdrop);
    font-family: "Open Sans", Arial, sans-serif;
  }
  .canvas {
    position: relative;
    width: 1200px;
    height: 900px;
    display: flex;
    align-items: center;
    justify-content: center;
    gap: 50px;
  }
  .card {
    position: relative;
    width: 500px;
    height: 290px;
    background: var(--card);
    border-radius: 18px;
    box-shadow: 0 10px 30px rgba(0,0,0,0.45);
    overflow: hidden;
  }

  /* Front: contact side */
  .card-front .brand-mark {
    position: absolute;
    left: 40px;
    top: 112px;
    display: flex;
    align-items: center;
    gap: 12px;
  }
  .brand-square {
    width: 22px;
    height: 22px;
    background: var(--accent);
  }
  .brand-name {
    font-size: 42px;
    font-weight: 700;
    color: var(--accent);
    letter-spacing: -0.5px;
    line-height: 1;
  }
  .contact {
    position: absolute;
    left: 286px;
    top: 34px;
    color: var(--text);
  }
  .contact-name {
    font-size: 15px;
    font-weight: 700;
    color: var(--accent);
    text-transform: uppercase;
    letter-spacing: 0.3px;
  }
  .contact-title {
    font-size: 11.5px;
    margin-top: 1px;
  }
  .contact-list {
    list-style: none;
    margin-top: 22px;
  }
  .contact-list li {
    display: flex;
    align-items: center;
    gap: 8px;
    font-size: 12.5px;
    line-height: 19px;
  }
  .contact-list svg {
    width: 11px;
    height: 11px;
    flex: none;
    fill: var(--accent);
  }
  .contact-address {
    font-size: 12.5px;
    line-height: 18px;
    margin-top: 10px;
    padding-left: 19px;
    font-style: normal;
  }

  /* Back: brand side */
  .card-back .brand-block {
    position: absolute;
    left: 0;
    right: 0;
    top: 108px;
    text-align: center;
  }
  .brand-lockup {
    display: inline-flex;
    align-items: center;
    gap: 12px;
  }
  .brand-lockup .brand-square {
    background: var(--silver);
    width: 20px;
    height: 20px;
  }
  .brand-lockup .brand-name {
    color: var(--silver);
    font-size: 34px;
  }
  .license {
    margin-top: 16px;
    font-size: 11px;
    color: var(--text);
  }
</style>
</head>
<body>
<main class="canvas">
  <section class="card card-front" aria-label="Business card front">
    <div class="brand-mark">
      <span class="brand-square"></span>
      <span class="brand-name">quarry</span>
    </div>
    <div class="contact">
      <h1 class="contact-name">Dorian Velkova</h1>
      <p class="contact-title">Home Comfort Consultant</p>
      <ul class="contact-list">
        <li>
          <svg viewBox="0 0 12 12"><path d="M1 4c0-2 2-3 5-3s5 1 5 3v1H8V4H4v1H1z M3 6h6l1 5H2z"/></svg>
          888-317-5069
        </li>
        <li>
          <svg viewBox="0 0 12 12"><path d="M3 0h6a1 1 0 0 1 1 1v10a1 1 0 0 1-1 1H3a1 1 0 0 1-1-1V1a1 1 0 0 1 1-1zm0 2v7h6V2z"/></svg>
          510-642-1388
        </li>
        <li>
          <svg viewBox="0 0 12 12"><path d="M0 2h12v8H0z M1 3v.5l5 3.5 5-3.5V3z" fill-rule="evenodd"/></svg>
          dorian@quarry-hvac.com
        </li>
        <li>
          <svg viewBox="0 0 12 12"><circle cx="6" cy="6" r="6"/></svg>
          quarry-hvac.com
        </li>
      </ul>
      <address class="contact-address">
        4827 Marrow Ridge Rd #215<br>
        Oakland, CA 94611
      </address>
    </div>
  </section>

  <section class="card card-back" aria-label="Business card back">
    <div class="brand-block">
      <div class="brand-lockup">
        <span class="brand-square"></span>
        <span class="brand-name">quarry home solutions</span>
      </div>
      <p class="license">Lic# 458127</p>
    </div>
  </section>
</main>
</body>
</html>
```